Landing page design for my current website

I need a landing page designed for my Wordpress website. My website is Plumvarick.com, and I need a page that will serve as a landing page for online ads I run. Please follow the color scheme of the current website

This web page will be targeted towards real estate owners who are looking for a property manager. Above the fold needs to have a CTA form headlined with "As a Rental Property Owner, I Want More Protection, Less Stress, and Drama-Free Living"

A few highlights that can be listed beyond the CTA and fold

- Comprehensive Property Management
Full-service management covering tenant placement, leasing, maintenance, and inspections.

Maximized Rental Income
Proven strategies to optimize rental rates and minimize vacancies, ensuring higher ROI.

Stress-Free Management
We handle all tenant interactions, maintenance requests, and property issues, so you don't have to.

Experienced Team
Over a decade of experience in managing single-family homes, small multifamily units, and apartment complexes.

Advanced Technology
Utilize cutting-edge property management software for efficient communication, rent collection, and maintenance tracking.

Tenant Screening and Placement
Thorough background checks and tenant screening processes to ensure reliable and responsible tenants.

Regular Property Inspections
Routine inspections to maintain property condition and address issues before they become costly problems.

Legal Compliance
Expertise in local and federal rental laws to keep your properties compliant and avoid legal hassles.

Transparent Reporting
Detailed monthly reports and financial statements to keep you informed about your property's performance.

Personalized Service
Tailored management plans to meet the unique needs of your properties and investment goals.
Effective Tenant Conflict Resolution
Skilled in handling challenging tenant situations, ensuring conflicts are resolved quickly and professionally to maintain a peaceful living environment and protect your investment.

```html
<!DOCTYPE html>
<html lang="en">
<head>
<meta charset="UTF-8">
<title>Plumvarick Realty – Property Management</title>
<link href="https://fonts.googleapis.com/css2?family=Montserrat:wght@400;500;600;700;800&family=Open+Sans:wght@400;600&display=swap" rel="stylesheet">
<style>
:root{
  --navy:#1b3a6b;
  --navy-dark:#132b52;
  --ink:#1f2937;
  --muted:#5f6b7a;
  --line:#d5dbe3;
  --hero-a:#e7ebf0;
  --hero-b:#c3cfdc;
  --band:#eef1f5;
  --white:#ffffff;
}
*{box-sizing:border-box;margin:0;padding:0}
html,body{width:900px;height:1200px;overflow:hidden}
body{background:var(--white);font-family:"Open Sans",Arial,sans-serif;color:var(--ink);position:relative}
.site-header{height:50px;display:flex;align-items:center;justify-content:space-between;padding:0 40px;background:var(--white);position:relative;z-index:2}
.brand{display:flex;align-items:center;gap:8px;font-family:"Montserrat",sans-serif;font-weight:700;font-size:13px;color:var(--navy);letter-spacing:.5px}
.brand-dot{width:26px;height:26px;border-radius:50%;background:var(--navy)}
.header-contact{display:flex;align-items:center;gap:8px;font-family:"Montserrat",sans-serif}
.header-contact svg{width:22px;height:22px}
.header-contact small{display:block;font-size:8px;color:var(--muted)}
.header-contact strong{font-size:12px;color:var(--navy)}

.hero{position:relative;height:380px;background:linear-gradient(90deg,var(--hero-a),var(--hero-b))}
.hero-photo{position:absolute;left:0;top:0;width:520px;height:380px;background:linear-gradient(135deg,#d9dfe6 0%,#aebccc 60%,#8d9fb4 100%)}
.lead-form{position:absolute;left:510px;top:20px;width:360px;background:var(--white);padding:20px 22px;box-shadow:0 8px 24px rgba(20,40,70,.18)}
.lead-form h1{font-family:"Montserrat",sans-serif;font-weight:700;font-size:14px;line-height:1.35;text-align:center;color:var(--navy);text-transform:uppercase}
.form-step{text-align:center;font-size:9px;color:var(--muted);margin:6px 0 10px;border-bottom:1px solid var(--line);padding-bottom:8px}
.field{margin-bottom:8px}
.field label{display:block;font-size:9px;font-weight:600;color:var(--ink);margin-bottom:3px}
.field-row{display:flex;gap:8px}
.input{height:24px;border:1px solid var(--line);flex:1;font-size:8px;color:#9aa4b1;padding:6px}
.btn-next{display:block;margin:10px auto 0;width:64px;height:24px;background:var(--navy);color:var(--white);font-family:"Montserrat",sans-serif;font-size:10px;font-weight:600;text-align:center;line-height:24px}

.features{position:absolute;top:430px;left:0;width:900px;height:480px}
.features h2{font-family:"Montserrat",sans-serif;font-weight:800;font-size:26px;color:var(--navy);text-align:center;text-transform:uppercase;letter-spacing:.5px}
.feature-col{position:absolute;top:80px;width:260px}
.feature-col.left{left:40px}
.feature-col.right{left:600px}
.feature{height:64px}
.feature h3{font-family:"Montserrat",sans-serif;font-size:12px;font-weight:700;color:var(--ink);margin-bottom:3px}
.feature p{font-size:8.5px;line-height:1.4;color:var(--muted)}
.feature-photo{position:absolute;left:335px;top:100px;width:230px;height:300px;background:linear-gradient(160deg,#cfd8e2,#8ea1b7)}
.badge{position:absolute;width:56px;height:56px;border-radius:50%;background:var(--white);border:4px solid var(--navy)}
.badge.top{left:305px;top:85px}
.badge.bottom{left:540px;top:360px}

.portal{position:absolute;top:925px;left:0;width:900px;height:215px;background:var(--band)}
.portal-copy{position:absolute;left:40px;top:30px;width:380px}
.portal-copy h2{font-family:"Montserrat",sans-serif;font-weight:700;font-size:28px;line-height:1.2;color:var(--navy)}
.portal-copy p{margin-top:12px;font-size:9.5px;line-height:1.5;color:var(--muted)}
.device-laptop{position:absolute;left:520px;top:25px;width:250px;height:160px;background:linear-gradient(180deg,#3a4350,#1d232b);border-radius:6px}
.device-phone{position:absolute;left:790px;top:75px;width:60px;height:115px;background:linear-gradient(180deg,#3a4350,#1d232b);border-radius:8px}

.site-footer{position:absolute;top:1140px;left:0;width:900px;height:60px;background:var(--navy);color:var(--white);display:flex;align-items:center;justify-content:space-between;padding:0 40px;font-size:9px}
.footer-contact li{list-style:none;display:flex;align-items:center;gap:5px;line-height:1.6}
.footer-contact svg{width:10px;height:10px}
.footer-contact .copy{opacity:.7;font-size:8px}
.footer-brand{display:flex;align-items:center;gap:8px;font-family:"Montserrat",sans-serif;font-weight:700;font-size:13px;letter-spacing:.5px}
.footer-brand .brand-dot{background:var(--white)}
</style>
</head>
<body>
<header class="site-header">
  <div class="brand"><span class="brand-dot"></span>PLUMVARICK REALTY</div>
  <div class="header-contact">
    <svg viewBox="0 0 24 24"><circle cx="12" cy="12" r="12" fill="#1b3a6b"/><path d="M8.5 6.5l2 2-1.2 1.6c.8 1.7 2 2.9 3.6 3.6l1.6-1.2 2 2-1.3 1.8C11 16 8 13 6.7 7.8z" fill="#fff"/></svg>
    <div><small>Call Us Today</small><strong>555.201.0480</strong></div>
  </div>
</header>

<section class="hero">
  <div class="hero-photo" role="img" aria-label="Smiling property manager in a suit holding a small model house"></div>
  <form class="lead-form">
    <h1>As a Rental Property Owner, I Want More Protection, Less Stress, and Drama-Free Living</h1>
    <div class="form-step">Step 1 of 2</div>
    <div class="field"><label>Your Name</label><div class="field-row"><div class="input">First Name</div><div class="input">Last Name</div></div></div>
    <div class="field"><label>Best Phone # To Contact You</label><div class="field-row"><div class="input">Phone</div></div></div>
    <div class="field"><label>Best Email To Contact You</label><div class="field-row"><div class="input">Email</div></div></div>
    <div class="field"><label>Your Home Address</label><div class="field-row"><div class="input">Street address, city, state</div></div></div>
    <div class="btn-next">Next</div>
  </form>
</section>

<section class="features">
  <h2>Not Your Average Landlord</h2>
  <div class="feature-col left">
    <div class="feature"><h3>Comprehensive Property Management</h3><p>Full-service management covering tenant placement, leasing, maintenance, and inspections.</p></div>
    <div class="feature"><h3>Maximized Rental Income</h3><p>Proven strategies to optimize rental rates and minimize vacancies, ensuring higher ROI.</p></div>
    <div class="feature"><h3>Stress-Free Management</h3><p>We handle all tenant interactions, maintenance requests, and property issues, so you don't have to.</p></div>
    <div class="feature"><h3>Experienced Team</h3><p>Over a decade of experience managing single-family homes, small multifamily units, and apartments.</p></div>
    <div class="feature"><h3>Advanced Technology</h3><p>Cutting-edge software for efficient communication, rent collection, and maintenance tracking.</p></div>
  </div>
  <div class="feature-photo" role="img" aria-label="Property manager holding a model house in front of a home"></div>
  <div class="badge top"></div>
  <div class="badge bottom"></div>
  <div class="feature-col right">
    <div class="feature"><h3>Tenant Screening and Placement</h3><p>Thorough background checks and screening to ensure reliable and responsible tenants.</p></div>
    <div class="feature"><h3>Regular Property Inspections</h3><p>Routine inspections to maintain condition and address issues before they become costly.</p></div>
    <div class="feature"><h3>Legal Compliance</h3><p>Expertise in local and federal rental laws to keep your properties compliant.</p></div>
    <div class="feature"><h3>Transparent Reporting</h3><p>Detailed monthly reports and financial statements on your property's performance.</p></div>
    <div class="feature"><h3>Personalized Service</h3><p>Tailored management plans to meet your properties' needs and investment goals.</p></div>
  </div>
</section>

<section class="portal">
  <div class="portal-copy">
    <h2>Your Lease. Your Rent.<br>Everything Online.</h2>
    <p>Plumvarick offers owners a secure online portal. Track rent payments, review statements, approve repairs and message our team anytime, from any device. Your property details stay organized, current and within easy reach.</p>
  </div>
  <div class="device-laptop" role="img" aria-label="Laptop showing the owner portal dashboard"></div>
  <div class="device-phone" role="img" aria-label="Phone showing the owner portal app"></div>
</section>

<footer class="site-footer">
  <ul class="footer-contact">
    <li><svg viewBox="0 0 24 24"><path d="M6 3l4 4-2 3c1.5 3 3 4.5 6 6l3-2 4 4-3 3C10 20 4 14 3 6z" fill="#fff"/></svg>555.201.0480</li>
    <li><svg viewBox="0 0 24 24"><rect x="2" y="5" width="20" height="14" fill="none" stroke="#fff" stroke-width="2"/><path d="M2 5l10 8 10-8" fill="none" stroke="#fff" stroke-width="2"/></svg>hello@plumvarick.com</li>
    <li class="copy">© 2024 Plumvarick Realty. All Rights Reserved.</li>
  </ul>
  <div class="footer-brand"><span class="brand-dot"></span>PLUMVARICK INC.</div>
</footer>
</body>
</html>
```